R7M Meridian Business Card Design

We need a business card created for our New Business "R7M Meridian"<br/><br/>The business card design is up to you however the following information must be on the business card:<br/><br/>Front of the business card -<br/>Email :dorianv@r7mmeridian.nz<br/>Mobile: +64 (0) 22 4871 659<br/>Website: www.r7mmeridian.nz<br/>Card Owner Name: Dorian Valcourt<br/>Company Title: Business Development Manager<br/>Slogan: "The BEST of both worlds". <br/>Logo On the front attached to the design brief<br/><br/>On the back: <br/>Space on the back for 4 more versions of the logo across the bottom of the card indicating different subsidiary brands - R7M Coffee, R7M Arts, R7M ?? (The card will be used for all of these brands - We Will add the extra subsidiary logos to the design once the design is finished (We are a graphics design team). <br/><br/>Other than that we want a premium feeling logo that remains universally usable depending on the business entity that we are using the card for. The use of bright bold colours would be great but we still want the card to feel premium.
Target Market(s)
Gift Design and Manufacturing Companies
Contact Information for Business Card
Front of the business card -
Email :dorianv@r7mmeridian.nz
Mobile: +64 (0) 22 4871 659
Website: www.r7mmeridian.nz
Card Owner Name: Dorian Valcourt
Company Title: Business Development Manager
Slogan: "The BEST of both worlds".
Logo On the front attached to the design brief

```html
<!DOCTYPE html>
<html lang="en">
<head>
<meta charset="utf-8">
<title>R7M Meridian — Business Card</title>
<link rel="stylesheet" href="https://fonts.googleapis.com/css2?family=Montserrat:wght@600;700&family=Lora:wght@400&family=Open+Sans:wght@400&display=swap">
<style>
  :root {
    --wood-dark: #2e1c12;
    --wood-mid: #5a3a25;
    --wood-warm: #74492c;
    --wood-light: #8a5a38;
    --box-dark: #16181c;
    --ribbon-teal: #1fa7a3;
    --name-blue: #2eaaf6;
    --text-white: #ffffff;
    --text-soft: #f3ece6;
  }
  html, body {
    margin: 0;
    padding: 0;
    width: 1200px;
    height: 706px;
    overflow: hidden;
    background: var(--wood-dark);
  }
  .card {
    position: relative;
    width: 1200px;
    height: 706px;
    overflow: hidden;
  }
  .card__backdrop {
    position: absolute;
    inset: 0;
    background:
      radial-gradient(ellipse 42% 55% at 88% 45%, var(--box-dark) 0%, rgba(22,24,28,0.85) 55%, rgba(22,24,28,0) 100%),
      radial-gradient(ellipse 70% 60% at 35% 75%, var(--wood-light) 0%, rgba(138,90,56,0) 70%),
      linear-gradient(160deg, var(--wood-dark) 0%, var(--wood-mid) 45%, var(--wood-warm) 75%, var(--wood-mid) 100%);
  }
  .card__name {
    position: absolute;
    left: 74px;
    top: 170px;
    margin: 0;
    font-family: "Montserrat", sans-serif;
    font-weight: 700;
    font-size: 56px;
    letter-spacing: 0.5px;
    line-height: 1;
    color: var(--name-blue);
    text-transform: uppercase;
  }
  .card__role {
    position: absolute;
    left: 76px;
    top: 262px;
    margin: 0;
    font-family: "Montserrat", sans-serif;
    font-weight: 700;
    font-size: 28px;
    line-height: 1;
    color: var(--text-white);
  }
  .card__contacts {
    position: absolute;
    left: 76px;
    top: 364px;
    margin: 0;
    padding: 0;
    list-style: none;
    font-family: "Lora", serif;
    font-size: 26px;
    line-height: 44px;
    color: var(--text-soft);
  }
  .card__slogan {
    position: absolute;
    left: 0;
    width: 1202px;
    top: 580px;
    margin: 0;
    text-align: center;
    font-family: "Open Sans", sans-serif;
    font-weight: 400;
    font-size: 48px;
    line-height: 1;
    color: var(--text-white);
  }
</style>
</head>
<body>
  <main class="card">
    <div class="card__backdrop" role="img" aria-label="Photograph of a dark wrapped gift box tied with a teal ribbon bow, resting on a warm brown wooden table"></div>
    <h1 class="card__name">Dorian Valcourt</h1>
    <p class="card__role">Business Development Manager</p>
    <ul class="card__contacts">
      <li>Mobile: +64 (0) 22 4871 659</li>
      <li>Email: dorianv@r7mmeridian.nz</li>
      <li>Website: www.r7mmeridian.nz</li>
    </ul>
    <p class="card__slogan">"The Best of Both Worlds"</p>
  </main>
</body>
</html>
```